Business card design needed

I am a free lance management consultant looking to have some professionally designed business cards created.
If possible if i could have some bullet points or something with a list of my services that would be great.
Services are:
- Strategic Planning
- Process Improvement
- Change Management
- IT Solutions & Implementation
- IT Consulting
- Web Solutions
Target Market(s)
Business Owners and Operators
Industry/Entity Type
Business
Contact Information for Business Card
Peter Whitlock
PW Consulting
0438 516 274
PETER@PETERWHITLOCK.EXAMPLE
www.peterwhitlock.example
Logo Text
PW Consulting
Logo styles of interest
Pictorial/Combination Logo
Wordmark Logo
Lettermark Logo
Look and feel
Each slider illustrates characteristics of the customer's brand and the style your logo design should communicate.

```html
<!DOCTYPE html>
<html lang="en">
<head>
<meta charset="utf-8">
<title>PW Consulting – Business Card</title>
<link rel="stylesheet" href="https://fonts.googleapis.com/css2?family=Montserrat:wght@600&family=Questrial&display=swap">
<style>
  :root {
    --ink: #333333;
    --ink-soft: #3d3d3d;
    --rule: #555555;
    --paper: #ffffff;
  }
  * { margin: 0; padding: 0; box-sizing: border-box; }
  html, body {
    width: 1200px;
    height: 693px;
    overflow: hidden;
    background: var(--paper);
  }
  .card {
    position: relative;
    width: 1200px;
    height: 693px;
    background: var(--paper);
    color: var(--ink);
    font-family: "Questrial", "Century Gothic", sans-serif;
  }
  .brand {
    position: absolute;
    left: 585px;
    top: 70px;
    transform: translateX(-50%);
    text-align: center;
    color: var(--ink);
    font-family: "Questrial", "Century Gothic", sans-serif;
    font-weight: 400;
  }
  .brand__monogram {
    display: block;
    font-size: 290px;
    line-height: 260px;
    letter-spacing: -4px;
  }
  .brand__word {
    display: block;
    font-size: 55px;
    line-height: 60px;
    letter-spacing: 2px;
    margin-top: 2px;
  }
  .contact {
    position: absolute;
    right: 660px;
    top: 422px;
    text-align: right;
    color: var(--ink);
  }
  .contact__name {
    font-family: "Montserrat", "Century Gothic", sans-serif;
    font-weight: 600;
    font-size: 44px;
    line-height: 46px;
    letter-spacing: 2px;
  }
  .contact__role {
    font-size: 15px;
    line-height: 18px;
    letter-spacing: 0.6px;
    margin-bottom: 14px;
  }
  .contact__line {
    font-size: 33px;
    line-height: 40px;
    letter-spacing: 0.8px;
    color: var(--ink-soft);
  }
  .divider {
    position: absolute;
    left: 585px;
    top: 420px;
    width: 1px;
    height: 211px;
    background: var(--rule);
  }
  .services {
    position: absolute;
    left: 625px;
    top: 422px;
    list-style: none;
    font-style: italic;
    font-size: 28px;
    line-height: 34.3px;
    letter-spacing: 1.4px;
    color: var(--ink-soft);
  }
</style>
</head>
<body>
  <main class="card">
    <div class="brand" aria-label="PW Consulting">
      <span class="brand__monogram">PW</span>
      <span class="brand__word">consulting</span>
    </div>

    <section class="contact">
      <h1 class="contact__name">PETER WHITLOCK</h1>
      <p class="contact__role">FREELANCE MANAGEMENT CONSULTANT</p>
      <p class="contact__line">0438 516 274</p>
      <p class="contact__line">peter@peterwhitlock.example</p>
      <p class="contact__line">www.peterwhitlock.example</p>
    </section>

    <div class="divider"></div>

    <ul class="services">
      <li>Strategic Planning</li>
      <li>Process Improvement</li>
      <li>Change Management</li>
      <li>IT Solutions &amp; Implementation</li>
      <li>IT Consulting</li>
      <li>Web Solutions</li>
    </ul>
  </main>
</body>
</html>
```